Luxury Skincare Product Box Packaging Design

Vorabelle is a range of skincare products that help protect, nourish, and strengthen even the most sensitive skin, ensuring it is healthy, glowing, calm, and soft. Skincare practices support skin to enhance its appearance and relieve skin conditions. Your skin reflects your health. It is your body canvas and is an asset. The products contain naturally derived ingredients, aromatherapy oils, sustainable and ethical ingredients, organic ingredients where possible, natural preservatives and Australian oils, fruits, and extracts.

Vorabelle
Tagline is "Where Calm Finds Bloom"

Our products do not contain sulphates, parabens, phthalates, petrochemicals, synthetic colours, nor synthetic fragrances.

Everything about the Vorabelle Skincare name is creative and communicates luxury. Vorabelle from your first glance of the name, you will know that this is a company with excellent products.

By keeping it simple, unique, and elegant is often associated with high quality and is a way to establish trust. Vorabelle is a product that is “pure” and natural, so Vorabelle packaging would look simple, elegant, and clean.

I have uploaded the actual logo design and individual labels for the current skincare range I currently with the ingredients included so you can get an understanding of what I like. I have also added samples of package designs I quite like to assist with your designs.

Each Product box packaging sizes are as follows:

Product One - Exfoliating Herbs: 110mm (H) x 33mm Diameter
Product Two - Probiotic Lotion: 138mm (H) x 33mm Diameter
Product Three - Vitamin A Serum: 120mm (H) x 30mm Diameter
Updates

The Measurements are as follows: Product One: 110mm (H) x 33mm Diameter Product Two: 138mm (H) x 33mm Diameter Product Three: 120mm (H) x 30mm Diameter

Target Market(s)

Women

Requirements
Must have
• Logo, Product Name and ingredients and if you can barcode on the packaging that is the box design I am after
Nice to have
• samples of designs I like but open to suggestions

```html
<!DOCTYPE html>
<html lang="en">
<head>
<meta charset="utf-8">
<title>Vorabelle Vitamin A Serum – Box Dieline and Bottle Label</title>
<link href="https://fonts.googleapis.com/css2?family=Marcellus&family=Playfair+Display:wght@600;700&family=Open+Sans:wght@400;600;700&display=swap" rel="stylesheet">
<style>
  :root {
    --paper: #ffffff;
    --ink: #1f1f1f;
    --copper: #a86f4e;
    --copper-light: #efbfa6;
    --mint: #bde0d0;
    --cut: #d8203c;
    --fold: #3bb4e6;
    --band-text: #ffffff;
  }
  html, body {
    margin: 0;
    width: 1200px;
    height: 1200px;
    overflow: hidden;
    background: var(--paper);
  }
  .canvas { position: relative; width: 1200px; height: 1200px; }
  .dieline { position: absolute; left: 20px; top: 140px; width: 662px; height: 919px; }
  .label { position: absolute; left: 690px; top: 560px; width: 490px; height: 404px; }

  .wordmark { font-family: "Marcellus", serif; fill: var(--ink); text-anchor: middle; }
  .mark-name { font-family: "Marcellus", serif; fill: var(--copper); text-anchor: middle; }
  .product-name { font-family: "Playfair Display", serif; font-weight: 700; fill: var(--ink); text-anchor: middle; }
  .tagline { font-family: "Playfair Display", serif; font-weight: 700; font-style: normal; fill: var(--ink); text-anchor: middle; }
  .body-copy { font-family: "Open Sans", sans-serif; fill: var(--ink); text-anchor: middle; }
  .heading { font-family: "Open Sans", sans-serif; font-weight: 700; fill: var(--ink); text-anchor: middle; }
  .icon-label { font-family: "Open Sans", sans-serif; fill: var(--ink); text-anchor: middle; }
  .band-text { font-family: "Open Sans", sans-serif; fill: var(--band-text); text-anchor: middle; }
  .volume { font-family: "Open Sans", sans-serif; fill: var(--ink); text-anchor: middle; }

  .cut-line { fill: none; stroke: var(--cut); stroke-width: 2; stroke-linejoin: round; }
  .fold-line { fill: none; stroke: var(--fold); stroke-width: 1.6; stroke-dasharray: 6 4; }
  .caution-box { fill: none; stroke: var(--ink); stroke-width: 1; stroke-dasharray: 2.5 2; }
  .icon { fill: none; stroke: var(--copper); stroke-width: 1.4; }
  .mark-ring { fill: none; stroke: var(--copper); stroke-width: 2; }
</style>
</head>
<body>
<div class="canvas">

  <!-- Carton dieline -->
  <svg class="dieline" viewBox="1170 25 735 1020" xmlns="http://www.w3.org/2000/svg">
    <defs>
      <linearGradient id="copperBand" x1="0" y1="0" x2="1" y2="0">
        <stop offset="0" stop-color="var(--copper)"/>
        <stop offset="0.3" stop-color="var(--copper-light)"/>
        <stop offset="0.55" stop-color="var(--copper)"/>
        <stop offset="0.8" stop-color="var(--copper-light)"/>
        <stop offset="1" stop-color="var(--copper)"/>
      </linearGradient>
    </defs>

    <!-- top flaps -->
    <path class="cut-line" fill="#fff" d="M1188 258 L1208 168 L1296 168 L1326 250 L1326 258 Z" style="fill:#fff"/>
    <path class="cut-line" style="fill:#fff" d="M1508 258 L1540 170 L1628 170 L1646 250 L1646 258 Z"/>
    <path class="cut-line" style="fill:#fff" d="M1646 258 L1646 122 L1672 122 L1672 130 L1800 130 L1800 122 L1828 122 L1828 258 Z"/>
    <path class="cut-line" style="fill:#fff" d="M1646 122 C1646 10 1828 10 1828 122"/>

    <!-- body panels -->
    <rect x="1175" y="258" width="680" height="458" fill="#fff"/>
    <rect x="1175" y="716" width="680" height="22" fill="url(#copperBand)"/>
    <rect x="1175" y="738" width="680" height="67" fill="var(--mint)"/>
    <path style="fill:#fff" d="M1828 258 L1897 270 L1897 716 L1828 716 Z"/>
    <path style="fill:var(--mint)" d="M1828 738 L1897 738 L1897 795 L1828 805 Z"/>
    <path class="cut-line" d="M1188 258 L1188 805 M1828 258 L1897 270 L1897 795 L1828 805"/>

    <!-- bottom flaps -->
    <path class="cut-line" style="fill:var(--mint)" d="M1188 805 L1215 890 L1306 890 L1326 812 L1326 805 Z"/>
    <path class="cut-line" style="fill:var(--mint)" d="M1508 805 L1530 890 L1620 890 L1646 812 L1646 805 Z"/>
    <path class="cut-line" style="fill:var(--mint)" d="M1326 805 L1326 942 L1354 942 L1354 935 L1482 935 L1482 942 L1508 942 L1508 805 Z"/>
    <path class="cut-line" style="fill:var(--mint)" d="M1326 942 C1326 1060 1508 1060 1508 942"/>

    <!-- fold lines -->
    <path class="fold-line" d="M1188 258 H1828 M1188 805 H1828 M1326 258 V805 M1508 258 V805 M1646 258 V805 M1828 258 V805 M1672 130 H1800 M1354 935 H1482"/>

    <!-- side panel: tagline -->
    <text class="tagline" font-size="17" transform="translate(1263 495) rotate(-90)">Where Calm Finds Bloom</text>

    <!-- front panel -->
    <circle class="mark-ring" cx="1417" cy="340" r="36"/>
    <text class="mark-name" x="1417" y="344" font-size="11">Vorabelle</text>
    <text class="wordmark" x="1417" y="428" font-size="32">Vorabelle</text>
    <text class="product-name" x="1418" y="648" font-size="19">Vitamin A</text>
    <text class="product-name" x="1418" y="672" font-size="19">Serum</text>

    <!-- side panel: claims -->
    <g>
      <circle class="icon" cx="1580" cy="398" r="9"/>
      <text class="icon-label" x="1580" y="418" font-size="5.5">Australian</text>
      <text class="icon-label" x="1580" y="425" font-size="5.5">made</text>
      <path class="icon" d="M1580 455 L1571 446 A5 5 0 0 1 1580 440 A5 5 0 0 1 1589 446 Z"/>
      <text class="icon-label" x="1580" y="464" font-size="5.5">100%</text>
      <text class="icon-label" x="1580" y="471" font-size="5.5">Vegan</text>
      <circle class="icon" cx="1580" cy="493" r="9"/>
      <text class="icon-label" x="1580" y="512" font-size="5.5">Cruelty</text>
      <text class="icon-label" x="1580" y="519" font-size="5.5">Free</text>
      <path class="icon" d="M1580 531 L1589 547 L1571 547 Z"/>
      <text class="icon-label" x="1580" y="557" font-size="5.5">Please</text>
      <text class="icon-label" x="1580" y="564" font-size="5.5">Recycle</text>
      <rect class="icon" x="1572" y="577" width="16" height="14" rx="2"/>
      <text class="icon-label" x="1580" y="603" font-size="5.5">6 months</text>
      <text class="icon-label" x="1580" y="610" font-size="5.5">once open</text>
    </g>

    <!-- back panel -->
    <g>
      <text class="product-name" x="1737" y="302" font-size="11">Vitamin A Serum</text>
      <text class="body-copy" font-size="7.2">
        <tspan x="1737" y="323">· All Skin Types ·</tspan>
        <tspan x="1737" y="334">Particularly beneficial for dry,</tspan>
        <tspan x="1737" y="345">Mature skin.</tspan>
        <tspan x="1737" y="361">...</tspan>
      </text>
      <text class="heading" x="1737" y="381" font-size="7.6">DIRECTIONS:</text>
      <text class="body-copy" font-size="6.6">
        <tspan x="1737" y="391">Massage a small amount into your</tspan>
        <tspan x="1737" y="401">face at night, avoiding eye area. Follow with</tspan>
        <tspan x="1737" y="411">your favourite moisturiser. Please note: Do not</tspan>
        <tspan x="1737" y="421">use on pregnant or breastfeeding women.</tspan>
      </text>
      <text class="heading" x="1737" y="453" font-size="7.6">INGREDIENTS:</text>
      <text class="body-copy" font-size="6.4">
        <tspan x="1737" y="465">SIMMONDSIA CHINENSIS (JOJOBA) SEED</tspan>
        <tspan x="1737" y="476.3">OIL*, PERSEA GRATISSIMA (AVOCADO) OIL,</tspan>
        <tspan x="1737" y="487.6">ROSA EGLANTERIA (ROSEHIP) OIL*, OLEA</tspan>
        <tspan x="1737" y="498.9">EUROPAEA (OLIVE) FRUIT OIL*, HIPPOPHAE</tspan>
        <tspan x="1737" y="510.2">RHAMNOIDES (SEABUCKTHORN BERRY)</tspan>
        <tspan x="1737" y="521.5">KERNAL EXTRACT*, TOCOPHEROL</tspan>
        <tspan x="1737" y="532.8">(VITAMIN E), RETINYL PALMITATE (VITAMIN</tspan>
        <tspan x="1737" y="544.1">A), GLYCINE SOJA OILBOSWELLIA CARTERII</tspan>
        <tspan x="1737" y="555.4">OIL (FRANKINCENSE), PELARGONIUM</tspan>
        <tspan x="1737" y="566.7">ROSEUM LEAF OIL, (ROSE GERANIUM),</tspan>
        <tspan x="1737" y="578">CANANGA ODORATA FLOWER OIL (YLANG</tspan>
        <tspan x="1737" y="589.3">YLANG), ROSMARINUS OFFICIANLIS LEAF</tspan>
        <tspan x="1737" y="600.6">EXTRACT</tspan>
        <tspan x="1737" y="611.9">*ORGANIC INGREDIENTS</tspan>
      </text>
      <text class="body-copy" x="1737" y="648" font-size="8">...</text>
      <rect class="caution-box" x="1656" y="661" width="162" height="39"/>
      <text class="body-copy" font-size="6.4">
        <tspan x="1737" y="673">Store in a cool dry place. Caution For</tspan>
        <tspan x="1737" y="683">external use only. Avoid contact with eyes.</tspan>
        <tspan x="1737" y="693">If irritation occurs, discontinue use.</tspan>
      </text>
    </g>

    <!-- bands -->
    <text class="band-text" x="1257" y="730" font-size="8">www.vorabelle.com</text>
    <text class="band-text" x="1418" y="731" font-size="11">All Skin Types</text>
    <text class="band-text" x="1580" y="730" font-size="8">www.vorabelle.com</text>
    <text class="volume" x="1418" y="767" font-size="11">30 ml</text>
    <text class="volume" x="1739" y="767" font-size="11">30 ml</text>
  </svg>

  <!-- Bottle label -->
  <svg class="label" viewBox="1243 1205 634 524" xmlns="http://www.w3.org/2000/svg">
    <defs>
      <linearGradient id="labelBand" x1="0" y1="0" x2="1" y2="0">
        <stop offset="0" stop-color="var(--copper)"/>
        <stop offset="0.3" stop-color="var(--copper-light)"/>
        <stop offset="0.6" stop-color="var(--copper)"/>
        <stop offset="0.85" stop-color="var(--copper-light)"/>
        <stop offset="1" stop-color="var(--copper)"/>
      </linearGradient>
      <clipPath id="labelShape"><rect x="1247" y="1208" width="625" height="517" rx="8"/></clipPath>
    </defs>
    <g clip-path="url(#labelShape)">
      <rect x="1247" y="1208" width="625" height="517" fill="#fff"/>
      <rect x="1247" y="1648" width="625" height="24" fill="url(#labelBand)"/>
      <rect x="1247" y="1672" width="625" height="53" fill="var(--mint)"/>
    </g>
    <rect x="1247" y="1208" width="625" height="517" rx="8" fill="none" stroke="var(--ink)" stroke-width="2.5"/>

    <circle class="mark-ring" cx="1398" cy="1310" r="42"/>
    <text class="mark-name" x="1398" y="1315" font-size="13">Vorabelle</text>
    <text class="wordmark" x="1393" y="1412" font-size="44">Vorabelle</text>
    <text class="product-name" x="1393" y="1592" font-size="22">Vitamin A</text>
    <text class="product-name" x="1393" y="1622" font-size="22">Serum</text>

    <g>
      <circle class="icon" cx="1560" cy="1278" r="13"/>
      <text class="icon-label" x="1560" y="1308" font-size="10">Australian</text>
      <text class="icon-label" x="1560" y="1321" font-size="10">made</text>
      <path class="icon" d="M1560 1364 L1546 1350 A7.5 7.5 0 0 1 1560 1341 A7.5 7.5 0 0 1 1574 1350 Z"/>
      <text class="icon-label" x="1560" y="1381" font-size="10">100%</text>
      <text class="icon-label" x="1560" y="1394" font-size="10">Vegan</text>
      <circle class="icon" cx="1560" cy="1425" r="13"/>
      <text class="icon-label" x="1560" y="1458" font-size="10">Cruelty</text>
      <text class="icon-label" x="1560" y="1471" font-size="10">Free</text>
      <path class="icon" d="M1560 1487 L1574 1512 L1546 1512 Z"/>
      <text class="icon-label" x="1560" y="1533" font-size="10">Please</text>
      <text class="icon-label" x="1560" y="1546" font-size="10">Recycle</text>
      <rect class="icon" x="1547" y="1567" width="26" height="20" rx="3"/>
      <text class="icon-label" x="1560" y="1610" font-size="10">6 months</text>
      <text class="icon-label" x="1560" y="1622" font-size="10">once open</text>
    </g>

    <g>
      <text class="product-name" x="1745" y="1257" font-size="14">Vitamin A Serum</text>
      <text class="body-copy" font-size="11.5">
        <tspan x="1745" y="1281">· All Skin Types ·</tspan>
        <tspan x="1745" y="1294">Particularly beneficial for dry,</tspan>
        <tspan x="1745" y="1307">Mature skin.</tspan>
        <tspan x="1745" y="1319">...</tspan>
      </text>
      <text class="heading" x="1745" y="1334" font-size="11.5">DIRECTIONS:</text>
      <text class="body-copy" font-size="11.2">
        <tspan x="1745" y="1347">Massage a small amount into your face at</tspan>
        <tspan x="1745" y="1360">night, avoiding eye area. Follow with your</tspan>
        <tspan x="1745" y="1373">favourite moisturiser. Please note: Do not</tspan>
        <tspan x="1745" y="1386">use on pregnant or breastfeeding women.</tspan>
        <tspan x="1745" y="1401">...</tspan>
      </text>
      <text class="heading" x="1745" y="1420" font-size="11.5">INGREDIENTS:</text>
      <text class="body-copy" font-size="10.2">
        <tspan x="1745" y="1433">SIMMONDSIA CHINENSIS (JOJOBA) SEED</tspan>
        <tspan x="1745" y="1444.6">OIL*, PERSEA GRATISSIMA (AVOCADO) OIL,</tspan>
        <tspan x="1745" y="1456.2">ROSA EGLANTERIA (ROSEHIP) OIL*, OLEA</tspan>
        <tspan x="1745" y="1467.8">EUROPAEA (OLIVE) FRUIT OIL*, HIPPOPHAE</tspan>
        <tspan x="1745" y="1479.4">RHAMNOIDES (SEABUCKTHORN BERRY)</tspan>
        <tspan x="1745" y="1491">KERNAL EXTRACT*, TOCOPHEROL (VITAMIN E),</tspan>
        <tspan x="1745" y="1502.6">RETINYL PALMITATE (VITAMIN A), GLYCINE</tspan>
        <tspan x="1745" y="1514.2">SOJA OILBOSWELLIA CARTERII OIL</tspan>
        <tspan x="1745" y="1525.8">(FRANKINCENSE), PELARGONIUM ROSEUM</tspan>
        <tspan x="1745" y="1537.4">LEAF OIL, (ROSE GERANIUM), CANANGA</tspan>
        <tspan x="1745" y="1549">ODORATA FLOWER OIL (YLANG YLANG),</tspan>
        <tspan x="1745" y="1560.6">ROSMARINUS OFFICIANLIS LEAF EXTRACT</tspan>
        <tspan x="1745" y="1572.2">*ORGANIC INGREDIENTS</tspan>
        <tspan x="1745" y="1586">...</tspan>
      </text>
      <rect class="caution-box" x="1645" y="1597" width="197" height="43"/>
      <text class="body-copy" font-size="10.2">
        <tspan x="1745" y="1611">Store in a cool dry place. Caution For</tspan>
        <tspan x="1745" y="1623">external use only. Avoid contact with eyes.</tspan>
        <tspan x="1745" y="1634">If irritation occurs, discontinue use.</tspan>
      </text>
    </g>

    <text class="band-text" x="1393" y="1665" font-size="11">All skin types</text>
    <text class="volume" x="1393" y="1701" font-size="13">30 ml</text>
    <text class="volume" x="1745" y="1702" font-size="14">www.vorabelle.com</text>
  </svg>

</div>
</body>
</html>
```